Small Business Consulting Firm Needs Business Card Design

Need a sleek modern business card with 2 sides matching the colors of our logo. We will be placing these with a mailer we are sending out. These business cards will only ever be given to business owners. We operate helping businesses who are struggling with cash flow or finances. If the green and blue design needs to be moved to the right of "Harborline Crest Consulting" for aesthetic purposes that is ok. We will need an editable file if possible. We would like to include the reps name, email, website, and phone number. For now just use Peter Vance, pvance@harborlinecrest.com, www.harborlinecrest.com, and 833-555-0172.

```html
<!DOCTYPE html>
<html lang="en">
<head>
<meta charset="UTF-8">
<title>Harborline Crest Consulting – Business Card</title>
<link href="https://fonts.googleapis.com/css2?family=Lato:wght@400;700&display=swap" rel="stylesheet">
<style>
  :root {
    --backdrop: #2b2e33;
    --card: #ffffff;
    --brand-blue: #1e7cc6;
    --brand-blue-deep: #1563a8;
    --brand-green: #6abf3b;
    --ink: #4a4d52;
    --on-blue: #ffffff;
  }
  * { margin: 0; padding: 0; box-sizing: border-box; }
  html, body {
    width: 1200px; height: 900px; overflow: hidden;
    background: var(--backdrop);
    font-family: "Lato", Arial, sans-serif;
  }
  .sheet {
    width: 1200px; height: 900px;
    display: flex; align-items: center; justify-content: center; gap: 40px;
  }
  .card {
    position: relative;
    width: 540px; height: 310px;
    background: var(--card);
    border-radius: 22px;
    overflow: hidden;
    box-shadow: 0 12px 30px rgba(0,0,0,.35);
  }
  .card__band { position: absolute; inset: 0; width: 100%; height: 100%; }

  .wordmark {
    display: flex; align-items: center; gap: 10px;
    color: var(--ink); font-weight: 400; text-transform: uppercase;
  }
  .wordmark__square { width: 22px; height: 22px; background: var(--brand-green); flex: none; }
  .wordmark__name { font-size: 15px; letter-spacing: 2.5px; line-height: 1.35; }

  .card--front .wordmark { position: absolute; left: 40px; top: 34px; }

  .rep { position: absolute; right: 34px; top: 136px; text-align: right; }
  .rep__name { color: var(--brand-green); font-weight: 700; font-size: 26px; letter-spacing: .5px; text-transform: uppercase; line-height: 1.2; }
  .rep__role { color: var(--brand-blue); font-size: 15px; margin-top: 2px; }

  .contacts { position: absolute; right: 30px; top: 226px; list-style: none; }
  .contacts li {
    display: flex; align-items: center; justify-content: flex-end; gap: 12px;
    color: var(--on-blue); font-size: 14.5px; height: 24px;
  }
  .contacts svg { width: 15px; height: 15px; flex: none; }

  .card--back { display: flex; align-items: center; justify-content: center; }
  .card--back .wordmark__square { width: 34px; height: 34px; }
  .card--back .wordmark__name { font-size: 22px; letter-spacing: 3.5px; }
</style>
</head>
<body>
<main class="sheet">
  <section class="card card--front" aria-label="Card front">
    <svg class="card__band" viewBox="0 0 540 310" preserveAspectRatio="none" aria-hidden="true">
      <defs>
        <linearGradient id="blueBand" x1="0" y1="0" x2="1" y2="1">
          <stop offset="0" stop-color="#2a8bd4"/>
          <stop offset="1" stop-color="#1563a8"/>
        </linearGradient>
      </defs>
      <path d="M0,150 C160,168 330,200 540,214 L540,310 L0,310 Z" fill="url(#blueBand)"/>
    </svg>

    <div class="wordmark">
      <span class="wordmark__square"></span>
      <span class="wordmark__name">Harborline Crest<br>Consulting</span>
    </div>

    <div class="rep">
      <p class="rep__name">Peter Vance</p>
      <p class="rep__role">Position</p>
    </div>

    <ul class="contacts">
      <li>833-555-0172
        <svg viewBox="0 0 24 24" aria-label="Phone"><path fill="#fff" d="M6.6 10.8a15 15 0 0 0 6.6 6.6l2.2-2.2a1 1 0 0 1 1-.25 11.4 11.4 0 0 0 3.6.57 1 1 0 0 1 1 1V20a1 1 0 0 1-1 1A17 17 0 0 1 3 4a1 1 0 0 1 1-1h3.5a1 1 0 0 1 1 1c0 1.250.2 2.450.57 3.57a1 1 0 0 1-.25 1z"/></svg>
      </li>
      <li>pvance@harborlinecrest.com
        <svg viewBox="0 0 24 24" aria-label="Email"><rect x="2" y="5" width="20" height="14" rx="1" fill="#fff"/><path d="M2 6l10 7 10-7" fill="none" stroke="#1e7cc6" stroke-width="1.8"/></svg>
      </li>
      <li>www.harborlinecrest.com
        <svg viewBox="0 0 24 24" aria-label="Website"><circle cx="12" cy="12" r="9.5" fill="none" stroke="#fff" stroke-width="2"/><path d="M2.5 12h19M12 2.5c3 3 3 16 0 19M12 2.5c-3 3-3 16 0 19" fill="none" stroke="#fff" stroke-width="1.6"/></svg>
      </li>
    </ul>
  </section>

  <section class="card card--back" aria-label="Card back">
    <div class="wordmark">
      <span class="wordmark__square"></span>
      <span class="wordmark__name">Harborline Crest<br>Consulting</span>
    </div>
  </section>
</main>
</body>
</html>
```